hi all

Im after a new age looking business card with my company logo on it

must include these details, I would like the PH and Email to be symbols

If the colours used for card could be kept within the colours used in logo that I have supplied that would be great, if another colour is to be used dark grey would be ok. no light bulbs etc thanks

Details below to be incorporated on card

Damian Holloway

Lic E871302

PH 0219647381

E info@brightvaleelectrical.example.nz

Domestic Commercial Industrial Electricians

```html
<!DOCTYPE html>
<html lang="en">
<head>
<meta charset="utf-8">
<title>Brightvale Electrical – Business Card</title>
<link rel="stylesheet" href="https://fonts.googleapis.com/css2?family=Jost:wght@400;500&display=swap">
<style>
  :root {
    --blue: #1f78c1;
    --black: #0b0b0b;
    --dark-grey: #3a3a3a;
    --white: #ffffff;
    --stage: #e6e8eb;
  }
  * { margin: 0; padding: 0; box-sizing: border-box; }
  html, body { width: 1200px; height: 791px; overflow: hidden; }
  body {
    background: var(--stage);
    font-family: "Jost", sans-serif;
    display: flex;
    align-items: center;
    justify-content: center;
    gap: 40px;
  }
  .card {
    position: relative;
    width: 520px;
    height: 297px;
    background: var(--white);
    box-shadow: 0 6px 18px rgba(0,0,0,.18);
    overflow: hidden;
  }

  /* Company name placeholder: one colour, one weight, one line */
  .brand {
    display: flex;
    align-items: center;
    gap: 10px;
    color: var(--blue);
    font-weight: 500;
    line-height: 1;
    white-space: nowrap;
  }
  .brand__dot {
    flex: none;
    border-radius: 50%;
    background: var(--blue);
  }

  /* Back face */
  .card--back .brand {
    position: absolute;
    left: 0; right: 0; top: 95px;
    justify-content: center;
    font-size: 34px;
  }
  .card--back .brand__dot { width: 22px; height: 22px; }
  .tagline-band {
    position: absolute;
    left: 0; right: 0; top: 188px;
    height: 38px;
    background: var(--blue);
    border-bottom: 5px solid var(--dark-grey);
    color: var(--white);
    font-size: 16.5px;
    font-weight: 500;
    letter-spacing: .6px;
    text-transform: uppercase;
    display: flex;
    align-items: center;
    justify-content: center;
    box-sizing: content-box;
  }

  /* Front face */
  .card--front .brand {
    position: absolute;
    left: 22px; top: 110px;
    font-size: 17px;
    gap: 7px;
  }
  .card--front .brand__dot { width: 12px; height: 12px; }
  .licence {
    position: absolute;
    left: 22px; bottom: 22px;
    font-size: 13px;
    color: var(--black);
    letter-spacing: .4px;
  }
  .divider { position: absolute; left: 208px; top: 0; width: 48px; height: 297px; }
  .panel {
    position: absolute;
    left: 236px; top: 0; right: 0; bottom: 0;
    background: var(--black);
    color: var(--white);
    padding: 34px 20px 0 38px;
  }
  .holder-name {
    font-size: 22px;
    font-weight: 400;
    letter-spacing: .8px;
    text-transform: uppercase;
  }
  .contacts { list-style: none; margin-top: 58px; }
  .contacts li {
    display: flex;
    align-items: center;
    gap: 10px;
    font-size: 12.5px;
    margin-bottom: 9px;
    margin-left: -30px;
  }
  .contacts svg { width: 20px; height: 20px; flex: none; }
  .services {
    margin-top: 30px;
    color: var(--blue);
    font-size: 14.5px;
    letter-spacing: .5px;
    text-transform: uppercase;
    line-height: 1.25;
  }
</style>
</head>
<body>

  <section class="card card--back" aria-label="Card back">
    <div class="brand">
      <span class="brand__dot"></span>
      <span class="brand__name">Brightvale Electrical</span>
    </div>
    <div class="tagline-band">Domestic Commercial Industrial Electricians</div>
  </section>

  <section class="card card--front" aria-label="Card front">
    <div class="brand">
      <span class="brand__dot"></span>
      <span class="brand__name">Brightvale Electrical</span>
    </div>
    <p class="licence">LIC E871302</p>

    <svg class="divider" viewBox="0 0 48 297" aria-hidden="true">
      <rect x="0" y="0" width="30" height="297" fill="var(--blue)"/>
      <rect x="10" y="-20" width="14" height="80" rx="7" fill="var(--black)"/>
      <rect x="10" y="236" width="14" height="90" rx="7" fill="var(--black)"/>
    </svg>

    <div class="panel">
      <h1 class="holder-name">Damian Holloway</h1>
      <ul class="contacts">
        <li>
          <svg viewBox="0 0 20 20" aria-label="Phone">
            <circle cx="10" cy="10" r="10" fill="var(--white)"/>
            <path d="M7 5.5c.5-.3 1-.2 1.3.3l.8 1.5c.2.4.1.8-.2 1.1l-.6.5c.5 1.1 1.4 2 2.5 2.6l.5-.6c.3-.3.7-.4 1.1-.2l1.5.8c.5.3.6.8.3 1.3l-.5.8c-.4.6-1.1.8-1.8.6-2.6-.9-4.6-2.9-5.5-5.5-.2-.7 0-1.4.6-1.8z" fill="var(--black)"/>
          </svg>
          <span>0219-647-381</span>
        </li>
        <li>
          <svg viewBox="0 0 20 20" aria-label="Email">
            <circle cx="10" cy="10" r="10" fill="var(--white)"/>
            <rect x="5" y="6.5" width="10" height="7" fill="var(--black)"/>
            <path d="M5.3 6.8 10 10.6l4.7-3.8" fill="none" stroke="var(--white)" stroke-width=".9"/>
          </svg>
          <span>info@brightvaleelectrical.example.nz</span>
        </li>
      </ul>
      <p class="services">Domestic Commercial<br>Industrial Electricians</p>
    </div>
  </section>

</body>
</html>
```